Plakat-Design für Werbung für ein Sägewerk
Zielgruppe
Sägewerk & Holzhandlung. Kanthölzer, Sparren, Latten und Bretter auf Wuschmaß.
Wir möchten ein Plakat als Werbung für unser Sägewerk.
Aufgabenstellung
Ansprechendes Design. Gut und Schnell Lesbar. Din A1 Querformat
Text: Sägewerk & Holzhandlung. Kanthölzer, Sparren, Latten und Bretter auf Wuschmaß. Sägewerk Trelkow, Kesselgrunder Str.4, 16542 Haselwerder OT Lindkamp, 0162/4391526, Kranzbergel@postmarkt-mail.de

```html
<!DOCTYPE html>
<html lang="de">
<head>
<meta charset="utf-8">
<title>Sägewerk Trelkow – Plakat</title>
<link href="https://fonts.googleapis.com/css2?family=Arvo:wght@700&family=Lexend:wght@500;700;800&display=swap" rel="stylesheet">
<style>
  :root {
    --brown: #4a2b2c;
    --green: #76b82a;
    --white: #ffffff;
    --page: #ffffff;
  }
  * { margin: 0; padding: 0; box-sizing: border-box; }
  html, body { width: 1200px; height: 1200px; overflow: hidden; background: var(--page); }
  .poster {
    position: absolute; left: 80px; top: 229px;
    width: 1041px; height: 735px;
    background: var(--white);
    box-shadow: 0 4px 14px rgba(0,0,0,.18);
    overflow: hidden;
    font-family: "Lexend", sans-serif;
  }
  .top-stripe { position: absolute; left: 0; top: 0; width: 100%; height: 15px; background: var(--green); }
  .header-band { position: absolute; left: 0; top: 15px; width: 100%; height: 100px; background: var(--brown); }
  .brand-title {
    position: absolute; left: 32px; top: 42px;
    font-family: "Arvo", serif; font-weight: 700; font-size: 51px; line-height: 1;
    color: var(--green); white-space: nowrap;
  }
  .wood-tile {
    position: absolute; left: 804px; top: 0; width: 202px; height: 115px;
    background: radial-gradient(circle at 40% 45%, #e0a36a 0%, #cf8a4f 40%, #b8743e 75%, #c98548 100%);
  }
  .headline {
    position: absolute; left: 30px; top: 124px; width: 1000px;
    font-weight: 800; font-size: 70px; line-height: 68px; letter-spacing: -0.5px;
    color: var(--brown); white-space: nowrap;
  }
  .headline .accent { color: var(--green); }
  .photo-yard {
    position: absolute; left: 0; top: 278px; width: 594px; height: 365px;
    background: linear-gradient(100deg, #c9a982 0%, #b88e63 40%, #6d6a6e 60%, #a98a6a 100%);
  }
  .photo-saw {
    position: absolute; left: 613px; top: 278px; width: 428px; height: 365px;
    background: linear-gradient(160deg, #e6d3b4 0%, #d8bd95 45%, #8f7458 75%, #6f7a4d 100%);
  }
  .footer-band { position: absolute; left: 0; top: 643px; width: 100%; height: 92px; background: var(--brown); }
  .company-name {
    position: absolute; left: 32px; top: 656px;
    font-family: "Arvo", serif; font-weight: 700; font-size: 34px; line-height: 1;
    color: var(--green);
  }
  .contact-line {
    position: absolute; left: 33px; top: 700px;
    font-weight: 500; font-size: 19.5px; line-height: 1; white-space: nowrap;
    color: var(--white);
  }
  .phone-box {
    position: absolute; left: 515px; top: 604px; width: 489px; height: 87px;
    background: var(--green); border: 3px solid var(--brown);
    display: flex; align-items: center; padding-left: 14px; gap: 16px;
  }
  .phone-box svg { width: 54px; height: 54px; flex: none; }
  .phone-number {
    font-weight: 700; font-style: italic; font-size: 49px; line-height: 1;
    color: var(--white); letter-spacing: -1px; white-space: nowrap;
  }
</style>
</head>
<body>
  <div class="poster">
    <div class="top-stripe"></div>
    <div class="header-band"></div>
    <div class="brand-title">Sägewerk &amp; Holzhandlung</div>
    <div class="wood-tile" role="img" aria-label="Holzquerschnitt mit Jahresringen und Maßband"></div>

    <h1 class="headline">Kanthölzer, Sparren, Latten<br>und Bretter <span class="accent">auf Wuschmaß!</span></h1>

    <div class="photo-yard" role="img" aria-label="Holzlager mit gestapelten Brettern und ein Arbeiter, der einen Balken trägt"></div>
    <div class="photo-saw" role="img" aria-label="Brett wird an einer Kreissäge zugeschnitten"></div>

    <div class="footer-band"></div>
    <div class="company-name">Sägewerk Trelkow</div>
    <div class="contact-line">Kesselgrunder Str.4 • 16542 Haselwerder OT Lindkamp • Kranzbergel@postmarkt-mail.de</div>

    <div class="phone-box">
      <svg viewBox="0 0 24 24" aria-hidden="true">
        <path fill="#ffffff" d="M6.6 10.8c1.4 2.8 3.8 5.1 6.6 6.6l2.2-2.2c.3-.3.7-.4 1-.2 1.1.4 2.3.6 3.6.6.6 0 1 .4 1 1V20c0 .6-.4 1-1 1C10.6 21 3 13.4 3 4c0-.6.4-1 1-1h3.5c.6 0 1 .4 1 1 0 1.3.2 2.5.6 3.6.1.3 0 .7-.2 1z"/>
      </svg>
      <span class="phone-number">0162 / 4391526</span>
    </div>
  </div>
</body>
</html>
```